Full Service Day Spa Needs Wordpress Template Designed

Willowmere Spa is a full service day spa, where we make our own line of bath and body products. The current website houses an online store with an ShopNexa base (as a WordPress plugin) and simple web pages with information and price lists for services.
For the upgraded website, we are doing a significant makeover and want to include the ability to have full screen video on our main page, windowed or full screen video on feature pages (for example, pages for "Meet our staff" or "Product Demos")
The site should retain standard WordPress compatibility for plugins, such as galleries etc.
The ability to include iframes would be considered a plus so that we can embed external scheduling applications that we subscribe to.
The color scheme for our spa features chocolate brown, taupe, cream, and turquoise for color accents. We would like our website to reflect these colors as our customers find them relaxing.
Our spa has a number of paintings on our walls, which could be used for inspiration for the website design. We like modern abstract art, with curves and swirls. I have included examples of this artwork so that potential designers can see what we like.
The new site must include our logo (provided) and our tag line: "Come Relax With Us" displayed in the upper left in the header.
We would prefer to have the option to put the menu either on the left side, or across the top to the right of the logo.
Words to describe the look we are seeking would be elegant, upscale, relaxing.

Target Market(s)

Our market is primarily local women (in and around our city) who are professionals aged 30 - 65.

Industry/Entity Type

Store

Colors
f78f20
00a990
f37022

Requirements
Must have
• The template should accommodate full screen and partial screen HTML5 video. Must have a menu, could be top or could be side. Should be in shades of browns and neutral colors, with teal accents, or similar highlights to the attached pictures of our artwork we have in the spa. We are looking for a consistent look that our customers can identify is us. Must have our logo in the upper left side of the header.
Nice to have
• Iframes built in would be nice, although we know we can get plugins for that. Likewise we know we can get plugins for the HTML 5 video, we would like the template built with accommodating that in mind. We have seen sites that have full screen video on the main page. We think this looks good.
Should not have
• We are looking for something elegant and upscale, so we are not looking for something "Cartoonish".

```html
<!DOCTYPE html>
<html lang="en">
<head>
<meta charset="utf-8">
<title>Willowmere Spa – Template Pages</title>
<link rel="stylesheet" href="https://fonts.googleapis.com/css2?family=Cormorant+Garamond:ital,wght@0,500;0,700;1,500&family=Arimo:wght@400;700&display=swap">
<style>
:root{
  --page:#ffffff;
  --header:#2a0f09;
  --choc:#3a1810;
  --choc-deep:#24100a;
  --nav:#5f4239;
  --nav-line:#8a6c62;
  --teal:#2ec9a2;
  --gold:#cfae6a;
  --taupe:#b79f8a;
  --cream:#f1e8da;
  --white:#ffffff;
  --field:#f3f3f3;
  --serif:"Cormorant Garamond", Georgia, serif;
  --sans:Arimo, Arial, sans-serif;
}
*{box-sizing:border-box;margin:0;padding:0}
html,body{width:1200px;height:1000px;overflow:hidden;background:var(--page)}
body{position:relative;font-family:var(--sans);color:var(--cream)}

.page{position:absolute;top:99px;width:354px;height:799px;overflow:hidden;
  background:radial-gradient(ellipse at 50% 55%,#4a2116 0%,var(--choc) 55%,var(--choc-deep) 100%)}
.page--home{left:39px}.page--shop{left:418px}.page--contact{left:797px}
.abs{position:absolute}

/* header */
.site-header{position:absolute;left:0;top:0;width:354px;height:60px;
  background:linear-gradient(180deg,#1f0a05,var(--header) 60%,#3a170d)}
.brand-mark{position:absolute;left:14px;top:10px;width:40px;height:40px;border-radius:50%;
  border:2px solid var(--gold)}
.brand-name{position:absolute;left:62px;top:8px;font-family:var(--serif);font-weight:700;
  font-size:21px;line-height:19px;color:var(--white);text-align:center}
.header-call{position:absolute;right:18px;top:24px;font-family:var(--serif);font-style:italic;
  font-size:16px;color:var(--white)}

/* hero */
.hero{position:absolute;left:0;top:60px;width:354px;height:161px}
.hero--video{background:linear-gradient(120deg,#6b3a26 0%,#c98e6d 40%,#e6b89a 60%,#4a2418 100%)}
.hero-caption{position:absolute;left:100px;top:130px;font-family:var(--sans);font-weight:700;
  font-size:12px;color:var(--white)}
.hero--products{background:linear-gradient(90deg,#c8642a 0%,#d9d1c8 18%,#b48ac6 32%,#e6e3d6 45%,#e9dc8c 58%,#d7d3cc 72%,#e7a3a3 86%,#cfc9c0 100%)}

/* nav */
.main-nav{position:absolute;left:0;top:221px;width:354px;height:15px;display:flex;
  background:var(--nav);border-top:1px solid var(--nav-line);border-bottom:1px solid var(--nav-line)}
.main-nav span{display:flex;align-items:center;justify-content:center;font-family:var(--serif);
  font-style:italic;font-size:10px;color:var(--white);border-right:1px solid var(--nav-line)}
.main-nav span:last-child{border-right:0}
.main-nav .is-active{background:var(--teal)}

/* type */
.section-title{position:absolute;width:354px;left:0;text-align:center;font-family:var(--serif);
  font-style:italic;font-weight:500;color:var(--taupe);font-size:23px}
.lead{position:absolute;left:40px;width:274px;text-align:center;font-family:var(--serif);
  font-style:italic;font-size:6.5px;line-height:8px;color:var(--white)}
.divider-ornament{position:absolute;left:137px;width:80px;height:12px;
  background:linear-gradient(90deg,transparent,rgba(183,159,138,.45),transparent)}

.feature{position:absolute;width:90px;text-align:center}
.feature-photo{width:60px;height:60px;margin:0 auto;border-radius:50%;border:3px solid #4b5a22}
.feature-name{margin-top:10px;font-family:var(--serif);font-style:italic;font-size:12px;color:var(--teal)}
.feature-text{margin-top:4px;font-family:var(--serif);font-style:italic;font-size:6.5px;line-height:8px;color:var(--white)}
.deal-frame{width:58px;height:30px;margin:8px auto 0;border:1.5px solid var(--taupe);border-radius:12px;
  display:flex;align-items:center;justify-content:center;font-family:var(--serif);font-style:italic;
  font-size:12px;color:var(--teal)}
.deal-text{margin-top:7px}

/* blog / sidebar */
.post-title{position:absolute;left:19px;top:275px;width:200px;font-family:var(--serif);font-style:italic;
  font-size:13px;line-height:16px;color:var(--gold);word-spacing:5px}
.post-photo{position:absolute;left:22px;top:325px;width:154px;height:114px;
  background:linear-gradient(135deg,#d9cfc6,#8a5b3c 45%,#5dc6d3 60%,#3a2418)}
.post-body{position:absolute;left:23px;top:450px;width:185px;font-size:6.2px;line-height:8.6px;
  text-align:justify;color:var(--white)}
.sidebar-rule{position:absolute;left:254px;top:266px;width:1px;height:428px;background:var(--taupe)}
.sidebar{position:absolute;left:267px;width:80px}
.sidebar-heading{font-family:var(--serif);font-style:italic;font-size:14px;color:var(--taupe);
  border-bottom:1px solid var(--taupe);padding-bottom:6px}
.sidebar-heading--plain{color:var(--white);border:0}
.sidebar-item{font-size:9.5px;color:var(--white);height:27px;display:flex;align-items:center;
  border-bottom:1px solid rgba(183,159,138,.7)}
.sidebar-item--plain{border:0}
.order-box{position:absolute;left:267px;top:571px;width:65px;height:120px;background:#6a5046;border-radius:4px;
  text-align:center}
.order-title{margin-top:4px;font-family:var(--serif);font-style:italic;font-size:10px;color:var(--white)}
.order-photo{width:59px;height:38px;margin:3px auto 0;background:linear-gradient(135deg,#7b6aa0,#cfc7da 55%,#4a3a5a)}
.order-text{margin:4px 5px 0;font-family:var(--serif);font-style:italic;font-size:5.6px;line-height:7px;
  text-align:justify;color:var(--white)}
.order-btn{width:40px;height:8px;margin:4px auto 0;border-radius:4px;background:var(--teal);
  font-size:5px;line-height:8px;color:var(--white)}

/* contact */
.form-heading{position:absolute;left:26px;font-family:var(--serif);font-style:italic;font-size:13px;color:var(--gold)}
.form-sub{position:absolute;left:24px;font-family:var(--serif);font-style:italic;font-size:10px;color:var(--taupe)}
.field{position:absolute;left:23px;width:112px;height:11px;background:var(--field)}
.field-label{position:absolute;left:140px;font-size:5.5px;color:var(--white)}
.textarea{position:absolute;left:23px;top:384px;width:208px;height:60px;background:var(--field)}
.submit{position:absolute;left:24px;top:457px;width:27px;height:9px;border-radius:4px;background:var(--teal);
  font-size:5px;line-height:9px;text-align:center;color:var(--white)}
.map{position:absolute;left:21px;top:511px;width:206px;height:129px;
  background:linear-gradient(135deg,#ece9e2,#dedbd3 50%,#e9e6de)}
.hours{position:absolute;left:26px;font-size:9px;color:var(--white)}

/* footer */
.site-footer{position:absolute;left:0;top:737px;width:354px;height:62px;background:#2a100a}
.footer-address{position:absolute;left:23px;top:12px;font-size:6.5px;line-height:8px;color:#c9bdb3}
.social{position:absolute;top:21px;width:10px;height:10px;border-radius:2px;background:#8d7a72}
.footer-call{position:absolute;left:252px;top:19px;font-family:var(--serif);font-style:italic;font-size:14px;color:var(--white)}
.footer-legal{position:absolute;left:0;top:54px;width:354px;text-align:center;font-size:4.5px;color:var(--white)}
</style>
</head>
<body>

<!-- HOME -->
<section class="page page--home">
  <header class="site-header">
    <div class="brand-mark"></div>
    <div class="brand-name">Willowmere<br>Spa</div>
    <div class="header-call">Call: 306 555 0142</div>
  </header>
  <div class="hero hero--video" role="img" aria-label="Photo of a relaxing back massage, to be replaced by a video">
    <span class="hero-caption">To be replaced by video</span>
  </div>
  <nav class="main-nav">
    <span style="width:51px">Home</span><span class="is-active" style="width:58px">Shop</span><span style="width:70px">Services</span><span style="width:50px">Contact</span><span style="width:68px">Price List</span><span style="width:57px">About</span>
  </nav>

  <div class="divider-ornament" style="top:248px" role="img" aria-label="Flourish ornament"></div>
  <h1 class="section-title" style="top:268px">Come Relax With Us</h1>
  <p class="lead" style="top:313px">It is a long established fact that a reader will be distracted by the readable content of a page when looking at its layout. The point of using Lorem Ipsum is that it has a more-or-less normal distribution of letters, as opposed to using 'Content here, content here'.</p>

  <div class="feature" style="left:15px;top:351px">
    <div class="feature-photo" role="img" aria-label="Photo of a manicure" style="background:linear-gradient(135deg,#e8c3a6,#b57c5b)"></div>
    <div class="feature-name">Nail</div>
    <p class="feature-text">It is a long established fact that a reader will be distracted.</p>
  </div>
  <div class="feature" style="left:124px;top:351px">
    <div class="feature-photo" role="img" aria-label="Photo of a facial massage" style="background:linear-gradient(135deg,#f0ddd0,#c29a82)"></div>
    <div class="feature-name">Massage</div>
    <p class="feature-text">It is a long established fact that a reader will be distracted.</p>
  </div>
  <div class="feature" style="left:234px;top:351px">
    <div class="feature-photo" role="img" aria-label="Photo of candles and spa stones" style="background:linear-gradient(135deg,#8a4a2c,#d7a070 60%,#5a2a1a)"></div>
    <div class="feature-name">Theraphy</div>
    <p class="feature-text">It is a long established fact that a reader will be distracted.</p>
  </div>

  <div class="divider-ornament" style="top:488px" role="img" aria-label="Flourish ornament"></div>
  <h2 class="section-title" style="top:506px">Best Deals for Members</h2>

  <div class="feature" style="left:16px;top:553px">
    <div class="feature-photo" role="img" aria-label="Photo of hands with a flower" style="background:linear-gradient(135deg,#f3ddd2,#d49a8a)"></div>
    <div class="deal-frame">On Sale</div>
    <p class="feature-text deal-text">It is a long established fact that a reader will be distracted.</p>
  </div>
  <div class="feature" style="left:124px;top:553px">
    <div class="feature-photo" role="img" aria-label="Illustration of a gold coin" style="background:radial-gradient(circle,#e8d28a,#b9953f)"></div>
    <div class="deal-frame">Rewards</div>
    <p class="feature-text deal-text">It is a long established fact that a reader will be distracted.</p>
  </div>
  <div class="feature" style="left:233px;top:553px">
    <div class="feature-photo" role="img" aria-label="Photo of a charm bracelet" style="background:linear-gradient(135deg,#3c2a22,#5fc2d0 50%,#7a5a40)"></div>
    <div class="deal-frame">Specials</div>
    <p class="feature-text deal-text">It is a long established fact that a reader will be distracted.</p>
  </div>

  <p class="lead" style="top:705px">It is a long established fact that a reader will be distracted by the readable content of a page when looking at its layout. The point of using Lorem Ipsum is that it has a more-or-less normal distribution of letters, as opposed to using 'Content here, content here'.</p>

  <footer class="site-footer">
    <div class="footer-address">Willowmere Spa<br>48-2210 Larkspur Rd<br>Brightwater, SK</div>
    <span class="social" style="left:121px"></span><span class="social" style="left:160px"></span><span class="social" style="left:198px"></span>
    <div class="footer-call">Call: 306 555 0142</div>
    <div class="footer-legal">Terms of Use | Privacy Policy | Sitemap &nbsp; © Copyright 2014: Willowmere Spa.</div>
  </footer>
</section>

<!-- SHOP -->
<section class="page page--shop">
  <header class="site-header">
    <div class="brand-mark"></div>
    <div class="brand-name">Willowmere<br>Spa</div>
    <div class="header-call">Call: 306 555 0142</div>
  </header>
  <div class="hero hero--products" role="img" aria-label="Photo of packaged wax melts in assorted scents"></div>
  <nav class="main-nav">
    <span style="width:51px">Home</span><span class="is-active" style="width:58px">Shop</span><span style="width:70px">Services</span><span style="width:50px">Contact</span><span style="width:68px">Price List</span><span style="width:57px">About</span>
  </nav>

  <h2 class="post-title">Now Available, Firebird Inspired Charm Bracelets</h2>
  <div class="post-photo" role="img" aria-label="Photo of a braided charm bracelet on a wrist"></div>
  <p class="post-body">It is a long established fact that a reader will be distracted by the readable content of a page when looking at its layout. The point of using Lorem Ipsum is that it has a more-or-less normal distribution of letters, as opposed to using 'Content here, content here', making it look like readable English. Many desktop publishing packages and web page editors now use Lorem Ipsum as their default model text, and a search for 'lorem ipsum' will uncover many web sites still in their infancy. Various versions have evolved over the years, sometimes by accident, sometimes on purpose (injected humour and the like).</p>

  <div class="sidebar-rule"></div>
  <div class="sidebar" style="top:268px">
    <div class="sidebar-heading">Categories</div>
    <div class="sidebar-item">post 1</div><div class="sidebar-item">post 2</div><div class="sidebar-item">post 3</div><div class="sidebar-item">post 4</div>
  </div>
  <div class="sidebar" style="top:418px">
    <div class="sidebar-heading sidebar-heading--plain">Archives</div>
    <div class="sidebar-item sidebar-item--plain">Archive 1</div><div class="sidebar-item sidebar-item--plain">Archive 2</div><div class="sidebar-item sidebar-item--plain">Archive 3</div><div class="sidebar-item sidebar-item--plain">Archive 4</div>
  </div>
  <div class="order-box">
    <div class="order-title">Order Now</div>
    <div class="order-photo" role="img" aria-label="Photo of a jar of body butter"></div>
    <p class="order-text">It is a long established fact that a reader will be distracted by the readable content of a page when looking at its layout.</p>
    <div class="order-btn">Click here</div>
  </div>

  <footer class="site-footer">
    <div class="footer-address">Willowmere Spa<br>48-2210 Larkspur Rd<br>Brightwater, SK</div>
    <span class="social" style="left:121px"></span><span class="social" style="left:160px"></span><span class="social" style="left:198px"></span>
    <div class="footer-call">Call: 306 555 0142</div>
    <div class="footer-legal">Terms of Use | Privacy Policy | Sitemap &nbsp; © Copyright 2014: Willowmere Spa.</div>
  </footer>
</section>

<!-- CONTACT -->
<section class="page page--contact">
  <header class="site-header">
    <div class="brand-mark"></div>
    <div class="brand-name">Willowmere<br>Spa</div>
    <div class="header-call">Call: 306 555 0142</div>
  </header>
  <div class="hero hero--products" role="img" aria-label="Photo of packaged wax melts in assorted scents"></div>
  <nav class="main-nav">
    <span style="width:51px">Home</span><span class="is-active" style="width:58px">Shop</span><span style="width:70px">Services</span><span style="width:50px">Contact</span><span style="width:68px">Price List</span><span style="width:57px">About</span>
  </nav>

  <h2 class="form-heading" style="top:272px">Contact Us</h2>
  <div class="form-sub" style="top:297px">Leave a reply</div>
  <div class="field" style="top:317px"></div><span class="field-label" style="top:320px">Name</span>
  <div class="field" style="top:338px"></div><span class="field-label" style="top:341px">Email</span>
  <div class="field" style="top:360px"></div><span class="field-label" style="top:363px">Website</span>
  <div class="textarea"></div>
  <div class="submit">Submit</div>

  <h2 class="form-heading" style="top:485px">Location</h2>
  <div class="map" role="img" aria-label="Street map showing the spa location"></div>

  <h2 class="form-heading" style="top:660px">Our opening hours</h2>
  <div class="hours" style="top:681px">what time open</div>
  <div class="hours" style="top:694px">what time close</div>

  <div class="sidebar-rule"></div>
  <div class="sidebar" style="top:268px">
    <div class="sidebar-heading">Categories</div>
    <div class="sidebar-item">post 1</div><div class="sidebar-item">post 2</div><div class="sidebar-item">post 3</div><div class="sidebar-item">post 4</div>
  </div>
  <div class="sidebar" style="top:418px">
    <div class="sidebar-heading sidebar-heading--plain">Archives</div>
    <div class="sidebar-item sidebar-item--plain">Archive 1</div><div class="sidebar-item sidebar-item--plain">Archive 2</div><div class="sidebar-item sidebar-item--plain">Archive 3</div><div class="sidebar-item sidebar-item--plain">Archive 4</div>
  </div>
  <div class="order-box">
    <div class="order-title">Order Now</div>
    <div class="order-photo" role="img" aria-label="Photo of a jar of body butter"></div>
    <p class="order-text">It is a long established fact that a reader will be distracted by the readable content of a page when looking at its layout.</p>
    <div class="order-btn">Click here</div>
  </div>

  <footer class="site-footer">
    <div class="footer-address">Willowmere Spa<br>48-2210 Larkspur Rd<br>Brightwater, SK</div>
    <span class="social" style="left:121px"></span><span class="social" style="left:160px"></span><span class="social" style="left:198px"></span>
    <div class="footer-call">Call: 306 555 0142</div>
    <div class="footer-legal">Terms of Use | Privacy Policy | Sitemap &nbsp; © Copyright 2014: Willowmere Spa.</div>
  </footer>
</section>

</body>
</html>
```